Skincare Cleanser Bottle Label

New product launch of a mint facial cleanser.
Brand is called Dorvella.
Product will be called Lumora.
Looking for a label design that can be printed using silk screening.
High gloss white plastic bottle. 8oz. White push pump top.
Clinical skincare brand, professional image, sold in medical spas.

Target Market(s)

Women Age 20-65

Industry/Entity Type

Health And Wellness

Font styles to use
Serif
Sans Serif

Requirements
Must have
• Dorvella brand name in the orignal font.
Should not have
• Multiple colours.

```html
<!DOCTYPE html>
<html lang="en">
<head>
<meta charset="utf-8">
<title>Dorvella Lumora – Mint Facial Cleanser Label</title>
<link href="https://fonts.googleapis.com/css2?family=Montserrat:wght@400;500;700&display=swap" rel="stylesheet">
<style>
  :root {
    --backdrop: #d8d7db;
    --label-white: #ffffff;
    --ink: #111111;
    --brand-grey: #4a4a4a;
    --reverse: #ffffff;
  }
  * { margin: 0; padding: 0; box-sizing: border-box; }
  html, body {
    width: 1200px;
    height: 1200px;
    overflow: hidden;
    background: var(--backdrop);
  }
  .canvas {
    position: relative;
    width: 1200px;
    height: 1200px;
    font-family: "Montserrat", sans-serif;
  }
  .label {
    position: absolute;
    left: 310px;
    top: 50px;
    width: 580px;
    height: 1100px;
    background: var(--label-white);
  }
  .brand-name {
    position: absolute;
    left: 135px;
    top: 560px;
    transform: translate(-50%, -50%) rotate(-90deg);
    font-size: 150px;
    font-weight: 500;
    letter-spacing: 2px;
    color: var(--brand-grey);
    line-height: 1;
    white-space: nowrap;
  }
  .product-block {
    position: absolute;
    left: 245px;
    top: 545px;
    width: 335px;
  }
  .product-name {
    background: var(--ink);
    color: var(--reverse);
    height: 140px;
    display: flex;
    align-items: center;
    padding-left: 32px;
    font-size: 44px;
    font-weight: 700;
    letter-spacing: 1px;
  }
  .product-descriptor {
    margin-top: 14px;
    padding-left: 8px;
    font-size: 22px;
    font-weight: 400;
    color: var(--ink);
    letter-spacing: 0.3px;
  }
  .volume {
    position: absolute;
    left: 0;
    right: 0;
    bottom: 60px;
    text-align: center;
    font-size: 16px;
    font-weight: 400;
    color: var(--ink);
    letter-spacing: 1px;
  }
</style>
</head>
<body>
  <main class="canvas">
    <section class="label">
      <div class="brand-name">dorvella</div>
      <div class="product-block">
        <div class="product-name">LUMORA</div>
        <div class="product-descriptor">MINT FACIAL CLEANSER</div>
      </div>
      <div class="volume">8.5 OZ. | 250 ML</div>
    </section>
  </main>
</body>
</html>
```